Media and Film Company Needs a New Website

We produce highly stylized commercials and film pieces for our clients. We also produce live events, both corporate and theatrical. Looking for a site that can show off our client videos - have a polished way to show off our team, and be able to create pages to highlight our clients and give a full overview of our project/process with them. We design simple website for some of our clients - so we are very wordpress familiar, and would like something that doesn't feel like a template.

Target Market(s)

content creators, creative directors, production teams, marketing agencies

Industry/Entity Type

Film Production

Number of Pages Required

4 page

Font styles to use
Sans Serif

Requirements
Must have
• slick looking video embed (from YT or Vimeo)
• project pages - client snapshot (what we did for them, how we did it)
• nice landing page, have our company video reel on the page
• testimonials
• contact page
• ability to have photos as a background if we want
Nice to have
• polished clean look - look to our logo colors and linear elements
• we produce very stylized videos for our clients and our website should reflect that
Should not have
• template look or feel to it- please bring your flare to the project!
• take a look at our current site - zantorvo.com we need a better way to highlight our work and our clients

```html
<!DOCTYPE html>
<html lang="en">
<head>
<meta charset="utf-8">
<title>Zantorvo – Contact</title>
<link href="https://fonts.googleapis.com/css2?family=Montserrat:wght@400;600;700&family=Open+Sans:wght@400;600&display=swap" rel="stylesheet">
<style>
:root{
  --ink:#1d1d1f;
  --night:#232325;
  --sky:#00b4ff;
  --blue:#0a6cff;
  --accent:#13a7f0;
  --panel:#ffffff;
  --rule:#dcdcdc;
  --card:#dedede;
  --muted:#8a8a8a;
  --thumb-a:#7a7f8c;
  --thumb-b:#c9b59c;
}
*{box-sizing:border-box;margin:0;padding:0}
html,body{width:684px;height:1200px;overflow:hidden}
body{background:var(--night);font-family:"Open Sans",sans-serif;color:var(--ink);position:relative}
.site-nav{position:absolute;top:0;left:0;width:684px;height:27px;background:var(--ink);display:flex;align-items:center}
.brand{position:absolute;left:74px;top:6px;font-family:"Montserrat",sans-serif;font-weight:700;font-size:12px;letter-spacing:1px;color:#fff;display:flex;align-items:center;gap:5px}
.brand-dot{width:9px;height:9px;border-radius:50%;background:var(--accent)}
.nav-links{position:absolute;left:172px;top:0;display:flex;gap:24px;list-style:none}
.nav-links li{font-family:"Montserrat",sans-serif;font-size:7px;font-weight:600;color:#e6e6e6;line-height:27px;letter-spacing:.4px}
.nav-links li.active{color:var(--accent);border-bottom:2px solid var(--accent)}
.hero{position:absolute;top:27px;left:0;width:684px;height:293px;background:linear-gradient(90deg,var(--sky),var(--blue))}
.hero h1{position:absolute;left:88px;top:70px;font-family:"Montserrat",sans-serif;font-weight:400;font-size:12px;color:#fff}
.hero .lead{position:absolute;left:88px;top:86px;width:200px;font-size:6.5px;line-height:9px;color:#e8f6ff}
.hero .rule{position:absolute;left:88px;top:170px;width:218px;height:1px;background:rgba(255,255,255,.6)}
.hero h2{position:absolute;left:88px;top:207px;font-family:"Montserrat",sans-serif;font-weight:400;font-size:11px;color:#fff}
.socials{position:absolute;left:88px;top:229px;display:flex;gap:7px}
.socials span{width:15px;height:15px;border-radius:50%;background:#fff;opacity:.9}
.message-form{position:absolute;left:376px;top:93px;width:221px}
.message-form h3{font-family:"Montserrat",sans-serif;font-size:6.5px;font-weight:600;color:#fff;margin-bottom:7px;letter-spacing:.3px}
.field{height:22px;background:#fff;margin-bottom:6px;font-size:6px;color:#9a9a9a;padding:7px 8px}
.field.area{height:72px}
.send{height:22px;background:var(--ink);color:#fff;font-family:"Montserrat",sans-serif;font-size:7px;font-weight:700;text-align:center;line-height:22px;margin-top:4px}
.content{position:absolute;left:73px;top:320px;width:538px;height:830px;background:var(--panel)}
.video-row{position:absolute;left:0;width:538px}
.row-title{position:absolute;left:16px;font-family:"Montserrat",sans-serif;font-size:6px;font-weight:600;color:#555;letter-spacing:.5px}
.thumb{position:absolute;width:103px;height:80px;background:linear-gradient(135deg,var(--thumb-a),var(--thumb-b));border:3px solid #fff;box-shadow:0 0 0 1px var(--rule)}
.play{position:absolute;left:36px;top:24px;width:26px;height:26px}
.feature{position:absolute;width:113px;height:188px;background:#fff;box-shadow:0 1px 6px rgba(0,0,0,.3);padding:5px}
.feature .thumb{position:relative;box-shadow:none;border:0;width:103px;height:86px}
.feature h4{font-size:6px;font-weight:600;margin:6px 0 3px}
.feature p{font-size:5.5px;line-height:8px;color:#777}
.divider{position:absolute;left:16px;width:506px;height:1px;background:var(--rule)}
.services-title{position:absolute;top:567px;width:538px;text-align:center;font-family:"Montserrat",sans-serif;font-size:10px;letter-spacing:1px;color:#555}
.services-title::before,.services-title::after{content:"";display:inline-block;width:150px;height:1px;background:var(--rule);vertical-align:middle;margin:0 12px}
.service{position:absolute;top:603px;width:116px;height:166px;background:var(--card);text-align:center;padding-top:14px}
.service.lead-card{background:var(--accent)}
.service svg{width:30px;height:30px}
.service h5{font-family:"Montserrat",sans-serif;font-size:7.5px;font-weight:700;line-height:10px;color:#3a3a3a;margin:6px 10px 5px;text-align:left}
.service.lead-card h5{color:#fff}
.service p{font-size:5px;line-height:7px;color:#6a6a6a;margin:0 10px;text-align:left}
.service.lead-card p{color:#eaf7ff}
.service .cta{position:absolute;left:18px;bottom:14px;width:80px;height:15px;background:#c8c8c8;color:#eee;font-size:5px;line-height:15px;font-family:"Montserrat",sans-serif;font-weight:600}
.service.lead-card .cta{background:var(--ink);color:#fff}
.site-footer{position:absolute;left:0;top:1150px;width:684px;height:50px;background:var(--ink)}
.site-footer small{position:absolute;left:10px;top:21px;font-size:6px;color:#cfcfcf;letter-spacing:.3px}
.site-footer .socials{left:544px;top:17px;gap:6px}
.site-footer .socials span{background:var(--accent);width:16px;height:16px}
</style>
</head>
<body>
<header class="site-nav">
  <div class="brand"><span class="brand-dot"></span>ZANTORVO</div>
  <ul class="nav-links">
    <li>HOME</li><li>PORTFOLIO</li><li>ABOUT US</li><li>TESTIMONIALS</li><li>PRESS</li><li class="active">CONTACT</li>
  </ul>
</header>

<section class="hero">
  <h1>Contact Us</h1>
  <p class="lead">Got a question? Send us a note and we will get back to you.</p>
  <div class="rule"></div>
  <h2>Connect with us</h2>
  <div class="socials"><span></span><span></span><span></span><span></span><span></span></div>
  <form class="message-form">
    <h3>SEND US A MESSAGE</h3>
    <div class="field">Your name</div>
    <div class="field">E-mail address</div>
    <div class="field">Phone Number</div>
    <div class="field area">Write your message here</div>
    <div class="send">SEND</div>
  </form>
</section>

<main class="content">
  <div class="row-title" style="top:18px">RECENTLY ADDED</div>
  <div class="thumb" style="left:20px;top:38px" role="img" aria-label="Video still from a recent project"><svg class="play" viewBox="0 0 26 26"><circle cx="13" cy="13" r="13" fill="#222" opacity=".8"/><path d="M10 7l9 6-9 6z" fill="#fff"/></svg></div>
  <div class="thumb" style="left:144px;top:38px" role="img" aria-label="Video still from a recent project"><svg class="play" viewBox="0 0 26 26"><circle cx="13" cy="13" r="13" fill="#222" opacity=".8"/><path d="M10 7l9 6-9 6z" fill="#fff"/></svg></div>
  <div class="feature" style="left:263px;top:34px">
    <div class="thumb" role="img" aria-label="Video still from a recent project"><svg class="play" viewBox="0 0 26 26"><circle cx="13" cy="13" r="13" fill="#222" opacity=".8"/><path d="M10 7l9 6-9 6z" fill="#fff"/></svg></div>
    <h4>Video Title</h4>
    <p>A short look at the shoot, the crew and the story behind it.</p>
  </div>
  <div class="thumb" style="left:398px;top:38px" role="img" aria-label="Video still from a recent project"><svg class="play" viewBox="0 0 26 26"><circle cx="13" cy="13" r="13" fill="#222" opacity=".8"/><path d="M10 7l9 6-9 6z" fill="#fff"/></svg></div>
  <div class="divider" style="top:235px"></div>

  <div class="row-title" style="top:250px">UPCOMING RELEASES</div>
  <div class="thumb" style="left:20px;top:272px" role="img" aria-label="Still from an upcoming release"><svg class="play" viewBox="0 0 26 26"><circle cx="13" cy="13" r="13" fill="#222" opacity=".8"/><path d="M10 7l9 6-9 6z" fill="#fff"/></svg></div>
  <div class="thumb" style="left:146px;top:272px" role="img" aria-label="Still from an upcoming release"><svg class="play" viewBox="0 0 26 26"><circle cx="13" cy="13" r="13" fill="#222" opacity=".8"/><path d="M10 7l9 6-9 6z" fill="#fff"/></svg></div>
  <div class="thumb" style="left:272px;top:272px" role="img" aria-label="Still from an upcoming release"><svg class="play" viewBox="0 0 26 26"><circle cx="13" cy="13" r="13" fill="#222" opacity=".8"/><path d="M10 7l9 6-9 6z" fill="#fff"/></svg></div>
  <div class="thumb" style="left:398px;top:272px" role="img" aria-label="Still from an upcoming release"><svg class="play" viewBox="0 0 26 26"><circle cx="13" cy="13" r="13" fill="#222" opacity=".8"/><path d="M10 7l9 6-9 6z" fill="#fff"/></svg></div>
  <div class="divider" style="top:388px"></div>

  <div class="row-title" style="top:405px">HALL OF FAME</div>
  <div class="thumb" style="left:20px;top:440px" role="img" aria-label="Still from a celebrated project"><svg class="play" viewBox="0 0 26 26"><circle cx="13" cy="13" r="13" fill="#222" opacity=".8"/><path d="M10 7l9 6-9 6z" fill="#fff"/></svg></div>
  <div class="thumb" style="left:146px;top:440px" role="img" aria-label="Still from a celebrated project"><svg class="play" viewBox="0 0 26 26"><circle cx="13" cy="13" r="13" fill="#222" opacity=".8"/><path d="M10 7l9 6-9 6z" fill="#fff"/></svg></div>
  <div class="thumb" style="left:272px;top:440px" role="img" aria-label="Still from a celebrated project"><svg class="play" viewBox="0 0 26 26"><circle cx="13" cy="13" r="13" fill="#222" opacity=".8"/><path d="M10 7l9 6-9 6z" fill="#fff"/></svg></div>
  <div class="thumb" style="left:398px;top:440px" role="img" aria-label="Still from a celebrated project"><svg class="play" viewBox="0 0 26 26"><circle cx="13" cy="13" r="13" fill="#222" opacity=".8"/><path d="M10 7l9 6-9 6z" fill="#fff"/></svg></div>
  <div class="divider" style="top:545px;left:0;width:538px"></div>

  <div class="services-title">WHAT WE DO</div>
  <div class="service" style="left:18px">
    <svg viewBox="0 0 30 30"><circle cx="9" cy="8" r="5" fill="#333"/><circle cx="19" cy="8" r="5" fill="#333"/><rect x="4" y="14" width="18" height="11" rx="1" fill="#333"/><path d="M22 17l6-3v11l-6-3z" fill="#333"/></svg>
    <h5>FILM AND MEDIA PRODUCTION</h5>
    <p>Commercials, short films and brand pieces shot end to end.</p>
    <div class="cta">GET STARTED</div>
  </div>
  <div class="service lead-card" style="left:148px">
    <svg viewBox="0 0 30 30"><rect x="4" y="12" width="22" height="14" fill="#222"/><path d="M4 6l21-4 1 6-21 4z" fill="#222"/><path d="M9 5l3 5M15 4l3 5M21 3l3 5" stroke="#fff" stroke-width="1.5"/></svg>
    <h5>LIVE PRODUCTION</h5>
    <p>Corporate and theatrical events staged, lit and filmed live.</p>
    <div class="cta">GET STARTED</div>
  </div>
  <div class="service" style="left:278px">
    <svg viewBox="0 0 30 30"><rect x="11" y="2" width="8" height="15" rx="4" fill="#333"/><path d="M7 13a8 8 0 0016 0" stroke="#333" stroke-width="2" fill="none"/><path d="M15 21v6M10 27h10" stroke="#333" stroke-width="2"/></svg>
    <h5>PR, MARKETING &amp; ADVERTISING</h5>
    <p>Campaigns, press outreach and ads that reach your audience.</p>
    <div class="cta">GET STARTED</div>
  </div>
  <div class="service" style="left:408px">
    <svg viewBox="0 0 30 30"><path d="M15 2l4 8.5 9 1-6.8 6.2 2 9L15 22l-8.2 4.7 2-9L2 11.5l9-1z" fill="#f5a623"/></svg>
    <h5>EVENTS</h5>
    <p>Launches, galas and showcases planned from start to finish.</p>
    <div class="cta">GET STARTED</div>
  </div>
</main>

<footer class="site-footer">
  <small>©2016 ZANTORVO MEDIA &amp; ENTERTAINMENT</small>
  <div class="socials"><span></span><span></span><span></span><span></span><span></span></div>
</footer>
</body>
</html>
```